Business card design needed

I would like a one sided black business card with the information provided above. Refer to my website www.lobcrafttennis.com.au for an example of colors I have used for my site, would like to keep this consistent for my business cards also, I will upload my logo below.

I am a new small business that provides tennis customers with racquet re stringing, tennis strings and accessories.

Industry/Entity Type

Small Business

Contact Information for Business Card

Lob Craft Tennis

Dennis Morrow
Managing Director

lobcrafttennis@mailbay.com
www.lobcrafttennis.com.au
0412 695 203

Racquet Restringing/Tennis Strings/Accessories

Requirements
Must have
• Must have my logo and card must be black

```html
<!DOCTYPE html>
<html lang="en">
<head>
<meta charset="utf-8">
<title>Lob Craft Tennis — Business Card</title>
<link href="https://fonts.googleapis.com/css2?family=Oswald:wght@400;500;600&display=swap" rel="stylesheet">
<style>
  :root {
    --page: #d9d9d9;
    --card: #050607;
    --card-glow: #121a22;
    --texture: #16212c;
    --text: #f2f2f2;
    --lime: #a8d94a;
    --rule: #2b3036;
  }
  * { box-sizing: border-box; margin: 0; padding: 0; }
  html, body { width: 1200px; height: 1200px; overflow: hidden; }
  body {
    background: var(--page);
    display: flex; align-items: center; justify-content: center;
    font-family: "Oswald", sans-serif;
  }
  .card {
    position: relative;
    width: 1050px; height: 600px;
    background: var(--card);
    color: var(--text);
    overflow: hidden;
    box-shadow: 0 20px 50px rgba(0,0,0,.25);
  }
  .card__texture {
    position: absolute; left: 0; top: 0; width: 100%; height: 70%;
    background: radial-gradient(ellipse 70% 80% at 30% 10%, var(--texture) 0%, transparent 75%);
  }
  .brand {
    position: absolute; left: 70px; top: 60px;
    display: flex; align-items: center; gap: 18px;
  }
  .brand__mark { width: 54px; height: 54px; border-radius: 50%; background: var(--lime); }
  .brand__name {
    font-size: 52px; font-weight: 600; letter-spacing: 3px;
    text-transform: uppercase; color: var(--lime);
  }
  .person {
    position: absolute; right: 70px; top: 185px; text-align: right;
    text-transform: uppercase; font-weight: 500; line-height: 1.15;
  }
  .person__name { font-size: 40px; letter-spacing: 1px; }
  .person__name .surname { color: var(--lime); }
  .person__role { font-size: 36px; letter-spacing: 1px; }
  .rule { position: absolute; height: 2px; background: linear-gradient(90deg, transparent, var(--rule) 20%, var(--rule) 80%, transparent); }
  .rule--top { left: 200px; right: 120px; top: 300px; }
  .rule--bottom { left: 180px; right: 240px; top: 450px; }
  .contact {
    position: absolute; left: 250px; top: 310px;
    list-style: none; text-transform: uppercase;
    font-size: 34px; font-weight: 500; line-height: 1.2;
  }
  .contact li { display: flex; align-items: center; gap: 14px; }
  .contact svg { width: 26px; height: 26px; flex: none; }
  .services {
    position: absolute; left: 180px; top: 480px;
    text-transform: uppercase; font-size: 27px; font-weight: 500; letter-spacing: .5px;
  }
</style>
</head>
<body>
  <article class="card">
    <div class="card__texture" role="img" aria-label="Soft dark-blue halftone texture across the upper card"></div>

    <header class="brand">
      <span class="brand__mark"></span>
      <span class="brand__name">Lob Craft Tennis</span>
    </header>

    <div class="person">
      <p class="person__name">Dennis <span class="surname">Morrow</span></p>
      <p class="person__role">Managing Director</p>
    </div>

    <div class="rule rule--top"></div>

    <ul class="contact">
      <li>
        <svg viewBox="0 0 24 24" aria-hidden="true"><rect x="2" y="5" width="20" height="14" fill="var(--lime)"/><path d="M2 5l10 8 10-8" fill="none" stroke="#050607" stroke-width="2"/></svg>
        lobcrafttennis@mailbay.com
      </li>
      <li>
        <svg viewBox="0 0 24 24" aria-hidden="true"><g fill="none" stroke="var(--lime)" stroke-width="2"><circle cx="12" cy="12" r="10"/><ellipse cx="12" cy="12" rx="4" ry="10"/><path d="M2 12h20M4 7h16M4 17h16"/></g></svg>
        www.lobcrafttennis.com.au
      </li>
      <li>
        <svg viewBox="0 0 24 24" aria-hidden="true"><path d="M6 2l4 4-2.5 2.5a12 12 0 0 0 8 8L18 14l4 4-3 3C10 21 3 14 3 5z" fill="var(--lime)"/></svg>
        0412 695 203
      </li>
    </ul>

    <div class="rule rule--bottom"></div>

    <p class="services">Racquet Restringing/Tennis Strings/Accessories</p>
  </article>
</body>
</html>
```